Hexagon Honey Bottle Design, simple and elegant.

Bottle description:
BODY HEIGHT With cap 8.75cm
Without cap 8.6cm
DIAMETER Inner 4.4cm
Outer 5.2cm
Label height only has to be = 6cm height x (3.4X6) length of one hexagonal box is 3.4cm
See through bottle with black cap.
Concept of design:
Elegant, Simple, no pictures of bees, pictures of honeycomb, wooden honey stick, or drooling honey from either is ok. Simple colors. (Designer's discretion)
Wordings:
Hex1
Product of Yemen
Header:
KORVAL /MELO/ (Brand name)
Explanatory below header
Yemen Sidr Honey from The Valley Ra'ufil (100% Pure)
(name of honey)
250g
Optional
Hex2
Pure
=
No Additives (not even natural additives)
Hex3
Raw
=
Unheated, Unpasteurized, Unprocessed honey
Hex4
Natural
=
No added color, artificial flavor, or synthetic substance
Hex5
RENOWNED
=
Very well known by honey lovers
(Natural Pure Raw and Renowned) wordings to be on a suitable place on the bottle (maybe on the cap) -
Hex6
Imported By
The Lantern Bazaar Pte Ltd
No. 317, Cobalt Ferry Road, #09-12
Cobalt Ferry Plaza
Singapore 195340
Wordings can be rearranged - its up to the designer's discretion where and how to place them and in which order.-
Designer must be willing to do numerous changes as the design develops

```html
<!DOCTYPE html>
<html lang="en">
<head>
<meta charset="utf-8">
<title>KORVAL /MELO/ Honey Jar Label</title>
<link href="https://fonts.googleapis.com/css2?family=Barlow+Condensed:wght@300;400;600&family=Jost:wght@300;400&display=swap" rel="stylesheet">
<style>
  :root {
    --backdrop: #5a5a5a;
    --label-tan: #c69c6d;
    --label-tan-light: #cfa97d;
    --label-line: rgba(255,255,255,0.25);
    --ink: #ffffff;
    --ink-soft: rgba(255,255,255,0.82);
    --comb-light: #f2f2f2;
    --comb-mid: #c9c9c9;
  }
  * { margin: 0; padding: 0; box-sizing: border-box; }
  html, body {
    width: 1200px; height: 1200px; overflow: hidden;
    background: var(--backdrop);
  }
  .canvas {
    width: 1200px; height: 1200px;
    display: flex; align-items: center; justify-content: center;
  }
  .label {
    width: 1140px; height: 335px;
    display: flex;
    background: var(--label-tan);
  }
  .panel {
    position: relative;
    width: 190px; height: 100%;
    border-right: 1px solid var(--label-line);
    color: var(--ink);
  }
  .panel:last-child { border-right: none; }
  .panel--light { background: var(--label-tan-light); }

  .comb-strip {
    position: absolute; top: 0; bottom: 0; width: 70px;
    background: linear-gradient(90deg, var(--comb-mid), var(--comb-light) 50%, var(--comb-mid));
  }
  .comb-strip--left { left: 70px; }
  .comb-strip--right { left: 50px; }

  /* front panel */
  .front {
    display: flex; flex-direction: column; align-items: center;
    text-align: center; padding: 26px 10px 28px;
    font-family: "Jost", sans-serif;
  }
  .front__origin { font-size: 19px; font-weight: 300; letter-spacing: 0.3px; }
  .front__brand {
    margin-top: 72px;
    font-family: "Barlow Condensed", sans-serif;
    font-weight: 600; font-size: 34px; letter-spacing: 0.5px;
  }
  .front__desc { margin-top: 14px; font-size: 13px; font-weight: 300; line-height: 1.5; }
  .front__weight { margin-top: auto; font-size: 14px; font-weight: 300; }

  /* qualities panel */
  .qualities {
    padding: 48px 14px 0;
    font-family: "Barlow Condensed", sans-serif;
    color: var(--ink-soft);
  }
  .quality { margin-bottom: 24px; }
  .quality__title { font-size: 19px; font-weight: 300; }
  .quality__text { font-size: 12px; font-weight: 300; line-height: 1.55; margin-top: 4px; }

  /* importer panel */
  .importer {
    padding: 80px 12px 0;
    font-family: "Barlow Condensed", sans-serif;
    font-weight: 400; font-size: 15.5px; line-height: 1.5;
    text-transform: uppercase;
  }

  /* renowned panel */
  .renowned {
    text-align: center; padding: 104px 14px 0;
    font-family: "Barlow Condensed", sans-serif;
    font-weight: 300;
  }
  .renowned__title { font-size: 19px; }
  .renowned__text { margin-top: 30px; font-size: 13px; line-height: 1.6; }
</style>
</head>
<body>
<main class="canvas">
  <section class="label" aria-label="Hexagonal jar label, unrolled">
    <div class="panel panel--side">
      <div class="comb-strip comb-strip--left" role="img" aria-label="Honeycomb pattern strip in white and grey"></div>
    </div>

    <div class="panel front">
      <p class="front__origin">Product of Yemen</p>
      <h1 class="front__brand">KORVAL/MELO/</h1>
      <p class="front__desc">Yemen Sidr Honey from The<br>Valley Ra'ufil<br>(100% pure)</p>
      <p class="front__weight">250g</p>
    </div>

    <div class="panel panel--light">
      <div class="comb-strip comb-strip--right" role="img" aria-label="Honeycomb pattern strip in white and grey"></div>
    </div>

    <div class="panel qualities">
      <div class="quality">
        <h2 class="quality__title">Pure</h2>
        <p class="quality__text">No additives (Not even<br>natural additives)</p>
      </div>
      <div class="quality">
        <h2 class="quality__title">Raw</h2>
        <p class="quality__text">Unheated, Unpasteurized,<br>Unprocessed honey</p>
      </div>
      <div class="quality">
        <h2 class="quality__title">Natural</h2>
        <p class="quality__text">No added color, artificial<br>flavor, or synthetic<br>substance</p>
      </div>
    </div>

    <div class="panel importer">
      <p>Imported by<br>
      The Lantern Bazaar Pte Ltd<br>
      No. 317, Cobalt Ferry Road,<br>
      #09-12<br>
      Cobalt Ferry Plaza<br>
      Singapore 195340</p>
    </div>

    <div class="panel panel--light renowned">
      <h2 class="renowned__title">Renowned</h2>
      <p class="renowned__text">Very well known by<br>honey lovers</p>
    </div>
  </section>
</main>
</body>
</html>
```